2024 Presentation for Job Interviews- I have been laid off

Refresh the branding and design to help create a dynamic presentation using some of Veltrano branding look and feel. This is a presentation I will use for interview processes with prospective employers. I would like it to be something that differentiates me from my competition
https://www.veltrano-example.com/c/en/us/about.html

Target Market(s)

Employers

Colors
0094D4
00A9DD
6FCCEA
C7EBF8
E9F6FB

```html
<!DOCTYPE html>
<html lang="en">
<head>
<meta charset="utf-8">
<title>Daniel Marsh — Americas Leader Presentation</title>
<link href="https://fonts.googleapis.com/css2?family=Montserrat:wght@400;500;600;700;800&display=swap" rel="stylesheet">
<style>
:root{
  --blue:#0094D4;
  --blue-2:#00A9DD;
  --blue-3:#6FCCEA;
  --blue-4:#C7EBF8;
  --blue-5:#E9F6FB;
  --navy:#0a1838;
  --navy-2:#10265a;
  --ink:#1b2233;
  --muted:#5b6475;
  --page:#0d0f14;
  --white:#ffffff;
}
*{box-sizing:border-box;margin:0;padding:0}
html,body{width:1200px;height:3884px;overflow:hidden}
body{background:var(--page);font-family:'Montserrat',sans-serif;color:var(--ink)}
.deck{display:flex;flex-direction:column;gap:16px;padding:12px 40px}
.slide{position:relative;width:1120px;height:630px;background:var(--white);overflow:hidden}
.slide-footer{position:absolute;right:28px;bottom:14px;font-size:9px;color:var(--muted)}
.slide-footer.light{color:rgba(255,255,255,.7)}
.photo{display:block}

/* cover */
.cover-hero{position:absolute;left:0;top:0;width:100%;height:440px;background:linear-gradient(180deg,#0b1436 0%,#1a2f72 45%,#2a5fb8 75%,#3e8fd8 100%)}
.cover-wave{position:absolute;left:0;top:330px}
.name-tag{position:absolute;left:22px;top:18px;background:var(--navy);color:var(--white);font-size:11px;font-weight:700;letter-spacing:.06em;padding:7px 12px;border:1px solid rgba(255,255,255,.4)}
.portrait{position:absolute;left:790px;top:270px;width:210px;height:210px;border-radius:50%;border:6px solid var(--white);background:linear-gradient(160deg,#8aa3b8,#3f5c7a);box-shadow:0 4px 12px rgba(0,0,0,.25)}
.cover-title{position:absolute;left:44px;top:470px}
.cover-title h1{font-size:34px;font-weight:800;line-height:1.15;color:var(--navy)}
.cover-title p{margin-top:6px;font-size:14px;font-weight:700;letter-spacing:.04em;color:var(--navy)}

/* values */
.values-head{text-align:center;padding-top:34px}
.values-head h2{font-size:30px;font-weight:800;color:var(--navy)}
.values-head p{margin-top:10px;font-size:12px;font-weight:700;letter-spacing:.03em;color:var(--ink)}
.values-grid{position:absolute;left:150px;top:120px;width:820px;display:flex;flex-direction:column;gap:6px}
.values-row{display:flex;gap:6px;height:150px}
.values-row .photo{flex:1;height:100%}
.tone-a{background:linear-gradient(135deg,#6b7d93,#2e3f55)}
.tone-b{background:linear-gradient(135deg,#a9b4c2,#5e6b7d)}
.tone-c{background:linear-gradient(135deg,#c48b6a,#6d4a3b)}
.tone-d{background:linear-gradient(135deg,#3c4656,#14181f)}
.tone-e{background:linear-gradient(135deg,#d7d2c8,#8e877b)}

/* impact */
.impact-text{position:absolute;left:44px;top:40px;width:560px}
.impact-text h2{font-size:30px;font-weight:800;color:var(--navy)}
.impact-text h3{margin-top:14px;font-size:19px;font-weight:800;color:var(--navy)}
.impact-text p{margin-top:12px;font-size:10.5px;line-height:1.55;color:var(--ink)}
.impact-photo{position:absolute;left:640px;top:110px;width:430px;height:420px;background:linear-gradient(160deg,#e6eef6,#b9c8d8 55%,#5f7a98)}

/* sponsors */
.sponsor-hero{position:absolute;left:0;top:0;width:100%;height:330px;background:linear-gradient(180deg,#0a1434 0%,#16306e 55%,#2f66b6 100%)}
.sponsor-wave{position:absolute;left:0;top:250px}
.sponsor-title{position:absolute;top:224px;width:100%;text-align:center;color:var(--white);font-size:22px;font-weight:800;letter-spacing:.06em}
.sponsor-list{position:absolute;left:60px;top:300px;width:1000px;display:flex;justify-content:space-between}
.sponsor{width:180px;text-align:center}
.sponsor .avatar{width:140px;height:140px;margin:0 auto;border-radius:50%;border:5px solid var(--white);background:linear-gradient(160deg,#b8c3cf,#56657a);box-shadow:0 3px 10px rgba(0,0,0,.2)}
.sponsor:nth-child(even){margin-top:-30px}
.sponsor h4{margin-top:12px;font-size:12px;font-weight:700;color:var(--navy)}
.sponsor p{margin-top:3px;font-size:9px;line-height:1.35;color:var(--muted)}

/* plan */
.slide.plan{background:var(--navy)}
.plan-backdrop{position:absolute;left:0;top:0;width:100%;height:100%;background:linear-gradient(180deg,#0a1838 0%,#0f2a5c 60%,#0c2148 100%)}
.plan-curves{position:absolute;left:0;top:0}
.plan-title{position:absolute;top:56px;width:100%;text-align:center;color:var(--white);font-size:24px;font-weight:800;letter-spacing:.02em}
.plan-cards{position:absolute;left:150px;top:150px;width:820px;display:flex;gap:20px}
.plan-card{flex:1;height:370px;background:var(--white);padding:30px 28px;box-shadow:0 6px 16px rgba(0,0,0,.3)}
.plan-icon{width:62px;height:62px;border-radius:50%;background:var(--blue);display:flex;align-items:center;justify-content:center}
.plan-card h3{margin-top:16px;font-size:19px;font-weight:800;color:var(--navy)}
.plan-card ul{margin-top:14px;list-style:none}
.plan-card li{position:relative;padding-left:16px;font-size:12px;line-height:2;color:var(--ink)}
.plan-card li::before{content:"";position:absolute;left:0;top:10px;width:7px;height:7px;background:var(--blue)}

/* thank you */
.thanks-photo{position:absolute;left:0;top:0;width:560px;height:630px;background:linear-gradient(150deg,#7d8a9a,#3c4a5e 55%,#1b2438)}
.thanks-panel{position:absolute;left:560px;top:0;width:560px;height:630px;background:var(--navy-2);padding:150px 0 0 90px;color:var(--white)}
.thanks-panel h2{font-size:30px;font-weight:800;letter-spacing:.03em}
.contact{margin-top:36px;display:flex;flex-direction:column;gap:26px}
.contact-item{display:flex;align-items:center;gap:16px}
.contact-icon{width:40px;height:40px;border-radius:50%;background:var(--blue);display:flex;align-items:center;justify-content:center;flex:none}
.contact-item .label{font-size:12px;font-weight:700}
.contact-item .value{font-size:12px;color:rgba(255,255,255,.85);line-height:1.4}
</style>
</head>
<body>
<main class="deck">

  <section class="slide cover">
    <div class="cover-hero photo" role="img" aria-label="Night city skyline with glowing blue light beams"></div>
    <svg class="cover-wave" width="1120" height="300" viewBox="0 0 1120 300">
      <path d="M0 120 C260 40 520 60 760 110 C900 140 1020 120 1120 70 L1120 300 L0 300 Z" fill="#ffffff"/>
      <path d="M0 112 C260 32 520 52 760 102 C900 132 1020 112 1120 62" fill="none" stroke="#0094D4" stroke-width="6"/>
      <path d="M0 100 C280 20 540 40 780 92 C920 120 1030 100 1120 50" fill="none" stroke="#6FCCEA" stroke-width="2"/>
    </svg>
    <div class="name-tag">DANIEL MARSH</div>
    <div class="portrait photo" role="img" aria-label="Headshot portrait of Daniel Marsh"></div>
    <div class="cover-title">
      <h1>Americas Leader<br>CISG | MIG Specialists</h1>
      <p>POINT OF VIEW DOCUMENT</p>
    </div>
    <div class="slide-footer">Daniel Marsh © 2024</div>
  </section>

  <section class="slide values">
    <div class="values-head">
      <h2>MY “WHAT MATTERS?”</h2>
      <p>SERVANT LEADERSHIP | “WHY WE CAN” MINDSET | CULTURE BY DESIGN | GOLDEN RULE | BE PRESENT</p>
    </div>
    <div class="values-grid">
      <div class="values-row">
        <div class="photo tone-a" style="flex:1.5" role="img" aria-label="Team group photo at an event"></div>
        <div class="photo tone-b" role="img" aria-label="Team gathered outdoors"></div>
        <div class="photo tone-c" role="img" aria-label="Volunteers at a charity event"></div>
      </div>
      <div class="values-row">
        <div class="photo tone-d" role="img" aria-label="Leader speaking on stage"></div>
        <div class="photo tone-e" role="img" aria-label="Colleagues celebrating together"></div>
        <div class="photo tone-a" role="img" aria-label="Award presentation"></div>
        <div class="photo tone-b" role="img" aria-label="Team dinner"></div>
      </div>
      <div class="values-row">
        <div class="photo tone-c" role="img" aria-label="Community volunteering day"></div>
        <div class="photo tone-d" style="flex:1.4" role="img" aria-label="Large team meeting"></div>
        <div class="photo tone-e" role="img" aria-label="Team members at a conference"></div>
      </div>
    </div>
    <div class="slide-footer">Daniel Marsh © 2024</div>
  </section>

  <section class="slide impact">
    <div class="impact-text">
      <h2>PEOPLE IMPACT</h2>
      <h3>PEOPLE DEVELOPMENT</h3>
      <p>I was able to get connected to Daniel through the mentoring program here at Veltrano. From the beginning, I sensed that our sessions would be incredibly valuable. Daniel focused on my goals and helped me build confidence in my leadership and my voice. His guidance helped me to step into a larger role as a Regional Manager and shaped how I lead my own team.</p>
      <p>Being chosen to participate in Daniel's Mentor Circle program proved to be a turning point for me in my journey as a leader. Getting the chance to speak openly with peers and learn from his experience gave me the tools I needed to grow. Daniel creates space for honest feedback and genuine support.</p>
      <p>I was able to grow my career with Daniel's mentorship, and his encouragement helped me earn a promotion. I am grateful for the time he invested in my development and I continue to apply the lessons he shared every single day.</p>
    </div>
    <div class="impact-photo photo" role="img" aria-label="Business team collaborating at a bright office table"></div>
    <div class="slide-footer">Daniel Marsh © 2024</div>
  </section>

  <section class="slide sponsors">
    <div class="sponsor-hero photo" role="img" aria-label="City skyline at night in blue tones"></div>
    <svg class="sponsor-wave" width="1120" height="380" viewBox="0 0 1120 380">
      <path d="M0 40 C300 110 600 110 860 60 C980 36 1060 40 1120 60 L1120 380 L0 380 Z" fill="#ffffff"/>
      <path d="M0 32 C300 102 600 102 860 52 C980 28 1060 32 1120 52" fill="none" stroke="#0094D4" stroke-width="6"/>
    </svg>
    <div class="sponsor-title">SPONSORS</div>
    <div class="sponsor-list">
      <div class="sponsor"><div class="avatar photo" role="img" aria-label="Portrait of Peter Alcott"></div><h4>Peter Alcott</h4><p>SVP Global Specialists</p></div>
      <div class="sponsor"><div class="avatar photo" role="img" aria-label="Portrait of Rob Hensley"></div><h4>Rob Hensley</h4><p>Global Head of Sales Solutions</p></div>
      <div class="sponsor"><div class="avatar photo" role="img" aria-label="Portrait of Will Danner"></div><h4>Will Danner</h4><p>SVP Global Sales<br>Veltrano</p></div>
      <div class="sponsor"><div class="avatar photo" role="img" aria-label="Portrait of Alan Kessler"></div><h4>Alan Kessler</h4><p>SVP Americas Service Provider<br>Veltrano</p></div>
      <div class="sponsor"><div class="avatar photo" role="img" aria-label="Portrait of Vera Lindqvist"></div><h4>Vera Lindqvist</h4><p>VP Americas Service Provider<br>Veltrano</p></div>
    </div>
    <div class="slide-footer">Daniel Marsh © 2024</div>
  </section>

  <section class="slide plan">
    <div class="plan-backdrop photo" role="img" aria-label="Dark blue financial market chart backdrop"></div>
    <svg class="plan-curves" width="1120" height="630" viewBox="0 0 1120 630">
      <path d="M760 0 C900 60 1000 60 1120 20" fill="none" stroke="#0094D4" stroke-width="6"/>
      <path d="M0 610 C300 560 700 560 1120 600" fill="none" stroke="#0094D4" stroke-width="5"/>
    </svg>
    <div class="plan-title">30-60-90 DAY PLAN</div>
    <div class="plan-cards">
      <article class="plan-card">
        <div class="plan-icon"><svg width="30" height="30" viewBox="0 0 24 24" fill="#fff"><circle cx="8" cy="8" r="3"/><circle cx="16" cy="8" r="3"/><path d="M2 20c0-4 3-6 6-6s6 2 6 6zM12 20c0-3 2-6 4-6 3 0 6 2 6 6z"/></svg></div>
        <h3>PEOPLE</h3>
        <ul><li>Build Trust</li><li>Key Stakeholders</li><li>Leadership Team</li><li>Sales Specialist Team</li><li>Engineering Team</li></ul>
      </article>
      <article class="plan-card">
        <div class="plan-icon"><svg width="30" height="30" viewBox="0 0 24 24" fill="#fff"><rect x="3" y="13" width="4" height="8"/><rect x="10" y="8" width="4" height="13"/><rect x="17" y="3" width="4" height="18"/></svg></div>
        <h3>PIPELINE</h3>
        <ul><li>Current Qtr &amp; Next Qtr Pipeline</li><li>Key Deals</li><li>Qtr Event Calendar</li><li>Sub $$ Portfolio Balance</li><li>2X2</li></ul>
      </article>
      <article class="plan-card">
        <div class="plan-icon"><svg width="30" height="30" viewBox="0 0 24 24" fill="none" stroke="#fff" stroke-width="2.2"><circle cx="12" cy="12" r="3"/><path d="M12 2v3M12 19v3M2 12h3M19 12h3M5 5l2 2M17 17l2 2M5 19l2-2M17 7l2-2"/></svg></div>
        <h3>PROCESS</h3>
        <ul><li>Team Cadence</li><li>Top / Down expectations</li><li>Bottom / Up expectations</li><li>Forecast Methodology</li><li>Reporting Packages</li><li>QBR vs. Reviews</li></ul>
      </article>
    </div>
    <div class="slide-footer light">Daniel Marsh © 2024</div>
  </section>

  <section class="slide thanks">
    <div class="thanks-photo photo" role="img" aria-label="Professionals in a meeting at a conference table"></div>
    <div class="thanks-panel">
      <h2>THANK YOU</h2>
      <div class="contact">
        <div class="contact-item">
          <div class="contact-icon"><svg width="18" height="18" viewBox="0 0 24 24" fill="#fff"><path d="M6.6 10.8a15 15 0 0 0 6.6 6.6l2.2-2.2c.3-.3.7-.4 1-.2 1.1.4 2.3.6 3.6.6.6 0 1 .4 1 1V20c0 .6-.4 1-1 1A17 17 0 0 1 3 4c0-.6.4-1 1-1h3.5c.6 0 1 .4 1 1 0 1.3.2 2.5.6 3.6.1.3 0 .7-.2 1z"/></svg></div>
          <div><div class="label">Phone</div><div class="value">+1 555 0100 2200</div></div>
        </div>
        <div class="contact-item">
          <div class="contact-icon"><svg width="18" height="18" viewBox="0 0 24 24" fill="#fff"><path d="M12 2a7 7 0 0 0-7 7c0 5 7 13 7 13s7-8 7-13a7 7 0 0 0-7-7zm0 9.5A2.5 2.5 0 1 1 12 6.5a2.5 2.5 0 0 1 0 5z"/></svg></div>
          <div><div class="label">Daniel Marsh</div><div class="value">520 enim ipsum voluptatem</div></div>
        </div>
        <div class="contact-item">
          <div class="contact-icon"><svg width="18" height="18" viewBox="0 0 24 24" fill="#fff"><path d="M3 5h18v14H3zm2 2v.5l7 4.5 7-4.5V7z"/></svg></div>
          <div><div class="label">Email</div><div class="value">info@danielmarsh-example.com</div></div>
        </div>
      </div>
    </div>
  </section>

</main>
</body>
</html>
```